Business Card Design Project

We need a Business Card for an Mechanical Engineering firm in Singapore. The design should be Modern & Technical looking, yet eye catching.

Our company deals in Cutting Tools & Machine Accessories for the Manufacturing Industries such as Oil & Gas, Aero Space, etc... For more information on our Company, you can either email me or view our website www.valtrion.com.sg.

We are trying to revamp our image to give our consumers a fresh new perspective to our company, so we welcome all ideas.

Industry/Entity Type

Business

Requirements
Must have
• Must incorporate New Company Logo into the card as shown in Uploaded file.

```html
<!DOCTYPE html>
<html lang="en">
<head>
<meta charset="utf-8">
<title>Valtrion Tools – Business Cards</title>
<link rel="stylesheet" href="https://fonts.googleapis.com/css2?family=PT+Sans+Narrow:wght@400;700&display=swap">
<style>
  :root {
    --page-bg: #efeae4;
    --maroon-dark: #3a121d;
    --maroon: #6d1a2c;
    --crimson: #951c35;
    --blush: #e6c3c9;
    --paper: #ffffff;
    --ink-light: #ffffff;
  }
  * { margin: 0; padding: 0; box-sizing: border-box; }
  html, body {
    width: 848px; height: 1200px; overflow: hidden;
    background: var(--page-bg);
    font-family: "PT Sans Narrow", "Arial Narrow", sans-serif;
  }
  .card {
    position: absolute;
    overflow: hidden;
    background: var(--paper);
    box-shadow: 0 6px 18px rgba(0,0,0,0.18);
  }
  .card-art { position: absolute; inset: 0; width: 100%; height: 100%; display: block; }
  .card--landscape { left: 124px; top: 70px; width: 600px; height: 345px; }
  .card--portrait { left: 251px; top: 480px; width: 345px; height: 600px; }

  .holder-name {
    position: absolute;
    color: var(--ink-light);
    font-size: 21px;
    line-height: 24px;
    letter-spacing: 0.3px;
    white-space: nowrap;
  }
  .contact-list {
    position: absolute;
    list-style: none;
    color: var(--ink-light);
    font-size: 16px;
    line-height: 19px;
    white-space: nowrap;
  }
  .brand {
    position: absolute;
    display: flex;
    align-items: center;
    gap: 8px;
    color: var(--crimson);
    font-size: 28px;
    line-height: 34px;
    font-weight: 400;
    letter-spacing: 1px;
    white-space: nowrap;
  }
  .brand-dot {
    width: 18px; height: 18px;
    border-radius: 50%;
    background: var(--crimson);
    flex: none;
  }

  .card--landscape .holder-name { left: 64px; top: 190px; }
  .card--landscape .contact-list { left: 70px; top: 228px; }
  .card--landscape .brand { left: 364px; top: 250px; }

  .card--portrait .brand { left: 40px; top: 150px; }
  .card--portrait .holder-name { left: 40px; top: 445px; }
  .card--portrait .contact-list--primary { left: 46px; top: 485px; }
  .card--portrait .contact-list--web { right: 34px; top: 395px; text-align: right; }
</style>
</head>
<body>

<section class="card card--landscape" aria-label="Business card, landscape">
  <svg class="card-art" viewBox="0 0 600 345" aria-hidden="true">
    <defs>
      <linearGradient id="maroonSweepH" x1="0" y1="0" x2="1" y2="0">
        <stop offset="0" stop-color="var(--maroon-dark)"/>
        <stop offset="1" stop-color="var(--crimson)"/>
      </linearGradient>
    </defs>
    <rect width="600" height="345" fill="url(#maroonSweepH)"/>
    <path d="M600,62 C470,90 330,200 286,345 L300,345 C350,215 470,108 600,86 Z" fill="var(--crimson)"/>
    <path d="M600,62 C470,90 330,200 286,345" fill="none" stroke="var(--blush)" stroke-width="2"/>
    <path d="M600,86 C470,108 350,215 300,345 L600,345 Z" fill="var(--paper)"/>
  </svg>
  <div class="brand"><span class="brand-dot"></span>VALTRION TOOLS</div>
  <p class="holder-name">YOUR NAME</p>
  <ul class="contact-list">
    <li>mobile:</li>
    <li>address</li>
    <li>website</li>
    <li>e-mail:</li>
  </ul>
</section>

<section class="card card--portrait" aria-label="Business card, portrait">
  <svg class="card-art" viewBox="0 0 345 600" aria-hidden="true">
    <defs>
      <linearGradient id="maroonSweepV" x1="0" y1="0" x2="1" y2="0">
        <stop offset="0" stop-color="var(--maroon-dark)"/>
        <stop offset="1" stop-color="var(--crimson)"/>
      </linearGradient>
    </defs>
    <rect width="345" height="600" fill="url(#maroonSweepV)"/>
    <path d="M0,0 H345 V160 C270,262 160,340 0,352 Z" fill="var(--paper)"/>
    <path d="M345,160 C270,262 160,340 0,352 L0,366 C150,360 262,300 345,186 Z" fill="var(--crimson)"/>
    <path d="M0,366 C150,360 262,300 345,186" fill="none" stroke="var(--blush)" stroke-width="2"/>
  </svg>
  <div class="brand"><span class="brand-dot"></span>VALTRION TOOLS</div>
  <ul class="contact-list contact-list--web">
    <li>website</li>
    <li>e-mail</li>
  </ul>
  <p class="holder-name">YOUR NAME</p>
  <ul class="contact-list contact-list--primary">
    <li>mobile:</li>
    <li>address</li>
  </ul>
</section>

</body>
</html>
```